Stationary & Business cards for Onsite Wastewater Company
Brindlecove Septic Systems Ltd.
Stationary & Business cards for Onsite Wastewater Company - Construction
Creative Brief
Professional
Dwight Amberole
6172 Pellworth St. Langley, B.C. V3K8R2
dwight@brindlecoveseptic-example.com
brindlecoveseptic-example.com
I would like it to say: Design & Build on the front of the card
Open to ideas: maybe use the logo with black background
lanternmoth lanternmoth

```html
<!DOCTYPE html>
<html lang="en">
<head>
<meta charset="utf-8">
<title>Brindlecove Septic Systems Ltd. — Stationery</title>
<link href="https://fonts.googleapis.com/css2?family=Montserrat:wght@800&family=Open+Sans:wght@400;600&display=swap" rel="stylesheet">
<style>
:root{
  --board:#b9b9b9;
  --paper:#ffffff;
  --ink:#111111;
  --blue:#1f7fc0;
  --grey-line:#c9c9c9;
  --muted:#555555;
}
*{box-sizing:border-box;margin:0;padding:0}
html,body{width:1200px;height:897px;overflow:hidden}
body{background:var(--board);font-family:"Open Sans",Arial,sans-serif;color:var(--ink);position:relative}
.board{position:absolute;inset:8px;border:1px solid #a9a9a9;background:linear-gradient(#bdbdbd,#b3b3b3)}
.piece{position:absolute;background:var(--paper);box-shadow:0 1px 4px rgba(0,0,0,.35);overflow:hidden}
.rounded{border-radius:10px}
.brand{font-family:"Montserrat",Arial,sans-serif;font-weight:800;color:var(--ink);letter-spacing:-.5px;line-height:1;position:absolute;text-transform:uppercase}
.band{position:absolute;left:0;bottom:0;width:100%}
.caption{position:absolute;font-size:7px;color:#444;text-align:center}
.small{font-size:5px;line-height:1.5;color:var(--muted);position:absolute}
.name{font-size:7px;position:absolute}
.rule{position:absolute;left:10%;right:10%;height:1px;background:var(--grey-line)}
.fax-title{position:absolute;font-size:22px;color:var(--blue);font-weight:600}
.field{position:absolute;font-size:5px;color:var(--muted);border-bottom:1px solid var(--grey-line);width:70px;padding-bottom:1px}
.check{position:absolute;font-size:4.5px;color:var(--muted)}
.check i{display:inline-block;width:4px;height:4px;border:1px solid #777;margin-right:2px;vertical-align:middle}
.blue-edge{position:absolute;top:0;bottom:0;width:10px;background:var(--blue)}
.pocket{position:absolute;bottom:0;background:var(--ink)}
.env-flap{position:absolute;left:0;width:100%}
</style>
</head>
<body>
<div class="board"></div>

<!-- business card front -->
<div class="piece rounded" style="left:36px;top:97px;width:189px;height:109px">
  <div class="brand" style="left:10px;top:12px;font-size:13px">Brindlecove</div>
  <div class="name" style="left:78px;top:46px">Dwight Amberole</div>
  <svg class="band" height="26" viewBox="0 0 100 26" preserveAspectRatio="none">
    <polygon points="0,12 100,8 100,14 0,15" fill="var(--blue)"/>
    <polygon points="55,14 100,10 100,26 45,26" fill="var(--ink)"/>
  </svg>
  <div class="small" style="right:8px;bottom:6px;color:#fff">604 555 0147</div>
</div>
<div class="caption" style="left:36px;top:208px;width:189px">Business Card Front</div>

<!-- business card back -->
<div class="piece rounded" style="left:36px;top:218px;width:189px;height:109px">
  <div class="brand" style="left:0;right:0;top:36px;text-align:center;font-size:16px">Brindlecove</div>
  <svg class="band" height="22" viewBox="0 0 100 22" preserveAspectRatio="none">
    <polygon points="0,10 100,6 100,12 0,13" fill="var(--blue)"/>
    <polygon points="55,12 100,8 100,22 45,22" fill="var(--ink)"/>
  </svg>
</div>

<!-- letterhead -->
<div class="piece" style="left:242px;top:41px;width:226px;height:371px">
  <div class="brand" style="left:12px;top:14px;font-size:14px">Brindlecove</div>
  <div class="small" style="right:14px;top:300px;text-align:right">6172 Pellworth St.<br>Langley, B.C. V3K8R2<br>604 555 0147<br>brindlecoveseptic-example.com</div>
  <svg class="band" height="26" viewBox="0 0 100 26" preserveAspectRatio="none">
    <polygon points="0,10 100,6 100,12 0,14" fill="var(--blue)"/>
    <polygon points="60,13 100,9 100,26 52,26" fill="var(--ink)"/>
  </svg>
</div>
<div class="caption" style="left:242px;top:414px;width:226px">Letterhead</div>

<!-- horizontal card -->
<div class="piece" style="left:548px;top:177px;width:169px;height:78px">
  <div class="brand" style="left:8px;top:8px;font-size:10px">Brindlecove</div>
  <svg class="band" height="18" viewBox="0 0 100 18" preserveAspectRatio="none">
    <polygon points="0,8 100,5 100,10 0,11" fill="var(--blue)"/>
    <polygon points="55,10 100,7 100,18 45,18" fill="var(--ink)"/>
  </svg>
</div>
<div class="caption" style="left:548px;top:257px;width:169px">Business Card</div>

<!-- vertical card -->
<div class="piece" style="left:739px;top:109px;width:97px;height:146px">
  <div class="brand" style="left:8px;top:10px;font-size:9px">Brindlecove</div>
  <div class="name" style="left:14px;top:40px;font-size:6px">Dwight Amberole</div>
  <svg class="band" height="20" viewBox="0 0 100 20" preserveAspectRatio="none">
    <polygon points="0,8 100,5 100,10 0,11" fill="var(--blue)"/>
    <polygon points="55,10 100,7 100,20 40,20" fill="var(--ink)"/>
  </svg>
</div>
<div class="caption" style="left:739px;top:257px;width:97px">Vertical Card</div>

<!-- compliment slip -->
<div class="piece" style="left:548px;top:310px;width:257px;height:102px">
  <div class="brand" style="left:10px;top:10px;font-size:11px">Brindlecove</div>
  <svg class="band" height="24" viewBox="0 0 100 24" preserveAspectRatio="none">
    <polygon points="0,10 100,6 100,12 0,13" fill="var(--blue)"/>
    <polygon points="58,12 100,8 100,24 48,24" fill="var(--ink)"/>
  </svg>
</div>
<div class="caption" style="left:548px;top:414px;width:257px">Compliment Slip</div>

<!-- envelopes -->
<div class="piece" style="left:877px;top:133px;width:282px;height:95px">
  <svg class="env-flap" style="top:0" height="40" viewBox="0 0 100 40" preserveAspectRatio="none">
    <polygon points="0,0 100,0 50,38" fill="var(--ink)"/>
    <polygon points="0,0 100,0 50,30" fill="var(--blue)"/>
    <polygon points="4,0 96,0 50,26" fill="#fff"/>
  </svg>
</div>
<div class="piece" style="left:877px;top:228px;width:282px;height:90px">
  <svg class="env-flap" style="top:0" height="70" viewBox="0 0 100 70" preserveAspectRatio="none">
    <polygon points="0,0 100,0 50,66" fill="var(--ink)"/>
    <polygon points="0,0 100,0 50,56" fill="var(--blue)"/>
    <polygon points="5,0 95,0 50,50" fill="#eee"/>
  </svg>
</div>
<div class="piece" style="left:877px;top:318px;width:282px;height:94px">
  <div class="brand" style="left:10px;top:10px;font-size:10px">Brindlecove</div>
  <svg class="band" height="22" viewBox="0 0 100 22" preserveAspectRatio="none">
    <polygon points="0,9 100,6 100,11 0,12" fill="var(--blue)"/>
    <polygon points="58,11 100,8 100,22 48,22" fill="var(--ink)"/>
  </svg>
</div>
<div class="caption" style="left:877px;top:414px;width:282px">Envelopes</div>

<!-- presentation folder -->
<div class="piece" style="left:85px;top:461px;width:473px;height:400px;background:#f4f4f4">
  <div class="blue-edge" style="left:0"></div>
  <div class="blue-edge" style="right:0"></div>
  <div style="position:absolute;left:236px;top:0;bottom:0;width:1px;background:#ddd"></div>
  <div class="brand" style="left:24px;top:120px;font-size:18px">Brindlecove</div>
  <div class="small" style="left:34px;top:150px">6172 Pellworth St.<br>Langley, B.C. V3K8R2<br>604 555 0147<br>dwight@brindlecoveseptic-example.com<br>brindlecoveseptic-example.com</div>
  <div class="brand" style="left:292px;top:12px;font-size:11px">Brindlecove</div>
  <div class="pocket" style="left:0;width:236px;height:150px;clip-path:polygon(0 15%,100% 0,100% 100%,0 100%)"></div>
  <div class="pocket" style="left:237px;width:236px;height:150px;clip-path:polygon(0 0,100% 15%,100% 100%,0 100%)"></div>
</div>
<div class="caption" style="left:85px;top:863px;width:473px">Presentation Folder</div>

<!-- notepad -->
<div class="piece" style="left:606px;top:461px;width:194px;height:358px">
  <div class="brand" style="left:8px;top:10px;font-size:10px">Brindlecove</div>
  <div class="rule" style="top:70px"></div><div class="rule" style="top:86px"></div>
  <div class="rule" style="top:102px"></div><div class="rule" style="top:118px"></div>
  <div class="rule" style="top:134px"></div><div class="rule" style="top:150px"></div>
  <div class="rule" style="top:166px"></div><div class="rule" style="top:182px"></div>
</div>
<div class="caption" style="left:606px;top:821px;width:194px">Notepad</div>

<!-- fax sheet -->
<div class="piece" style="left:824px;top:461px;width:223px;height:368px">
  <div class="brand" style="left:10px;top:12px;font-size:11px">Brindlecove</div>
  <div class="small" style="right:10px;top:10px;text-align:right">6172 Pellworth St.<br>Langley, B.C. V3K8R2</div>
  <div class="fax-title" style="left:10px;top:58px">Fax</div>
  <div class="field" style="left:10px;top:90px">To:</div><div class="field" style="left:120px;top:90px">From:</div>
  <div class="field" style="left:10px;top:102px">Fax:</div><div class="field" style="left:120px;top:102px">Pages:</div>
  <div class="field" style="left:10px;top:114px">Phone:</div><div class="field" style="left:120px;top:114px">Date:</div>
  <div class="field" style="left:10px;top:126px">Re:</div><div class="field" style="left:120px;top:126px">CC:</div>
  <div class="check" style="left:10px;top:140px"><i></i>Urgent</div>
  <div class="check" style="left:45px;top:140px"><i></i>For Review</div>
  <div class="check" style="left:88px;top:140px"><i></i>Please Comment</div>
  <div class="check" style="left:140px;top:140px"><i></i>Please Reply</div>
  <div class="check" style="left:182px;top:140px"><i></i>Recycle</div>
  <svg class="band" height="26" viewBox="0 0 100 26" preserveAspectRatio="none">
    <polygon points="0,10 100,6 100,12 0,14" fill="var(--blue)"/>
    <polygon points="60,13 100,9 100,26 52,26" fill="var(--ink)"/>
  </svg>
</div>
<div class="caption" style="left:824px;top:831px;width:223px">Fax Sheet</div>
</body>
</html>
```